Brantley Advisory Group provides support for renewable energy projects to utilities and suppliers

I need a professional looking business card that is both simple and elegant and unique. My clients are mostly large organizations not individuals. I am a consultant with my own company that is small but would like to give clients the impression I am larger. Smart grid, fiber optics, software, field hardware, distribution automation, substation automation, operations, energy storage/batteries, microgrids, customer service, strategy/roadmaps, conservation, Automated Metering Infrastruture (AMI or smart meters) are all areas of focus.

Target Market(s)

Utilities, suppliers, governmental agencies involved in energy. All types of energy especially natural gas and electrical. Especially renewable energy or green projects.

Contact Information for Business Card

Name - Mark Brantley Cell Phone - 425.318.2746 Email - mbrantley@brantleyag-example.com
Company - Brantley Advisory Group (logo) Title - Principal

Font styles to use
Serif
Sans Serif

Colors

Designer to choose colors to be used in the design.

Requirements
Must have
• Simple and professional and powerful.
• Unique/creative design.
Nice to have
• Utilize color scheme to accent logo colors. Maybe some geometric pattern on edge of card with color.
Should not have
• Busy, complicated, traditional

```html
<!DOCTYPE html>
<html lang="en">
<head>
<meta charset="utf-8">
<title>Brantley Advisory Group – Business Card</title>
<link rel="stylesheet" href="https://fonts.googleapis.com/css2?family=Alegreya+Sans:wght@400;500;700&family=Alegreya+Sans+SC:wght@400&display=swap">
<style>
  :root {
    --backdrop: #505457;
    --card: #1f1e20;
    --pattern: #3a393c;
    --blue: #3f5fc6;
    --green: #6aa33c;
  }
  * { box-sizing: border-box; margin: 0; padding: 0; }
  html, body { width: 1200px; height: 900px; overflow: hidden; }
  body {
    background: var(--backdrop);
    font-family: "Alegreya Sans", sans-serif;
    display: flex;
    align-items: center;
    justify-content: center;
    gap: 40px;
  }
  .card {
    position: relative;
    width: 540px;
    height: 309px;
    background: var(--card);
    border-radius: 16px;
    overflow: hidden;
    box-shadow: 0 14px 30px rgba(0,0,0,.45);
  }
  .pattern-field {
    position: absolute;
    pointer-events: none;
  }
  .card--contact .pattern-field--edge {
    left: 0; top: 0; bottom: 0; width: 120px;
    background: linear-gradient(90deg, var(--pattern), rgba(58,57,60,0));
  }
  .card--contact .pattern-field--corner {
    right: 0; bottom: 0; width: 300px; height: 200px;
    background: radial-gradient(ellipse at 100% 100%, var(--pattern) 0%, rgba(58,57,60,0) 70%);
  }
  .card--brand .pattern-field--corner {
    right: 0; bottom: 0; width: 420px; height: 230px;
    background: radial-gradient(ellipse at 100% 100%, var(--pattern) 0%, rgba(58,57,60,0) 70%);
  }
  .card--brand .pattern-field--top {
    left: 0; top: 0; width: 300px; height: 120px;
    background: radial-gradient(ellipse at 0% 0%, var(--pattern) 0%, rgba(58,57,60,0) 70%);
  }
  .brand {
    position: absolute;
    display: flex;
    align-items: center;
    gap: 12px;
    color: var(--blue);
    font-weight: 700;
    line-height: 1;
  }
  .brand__square {
    border: 3px solid var(--green);
    border-radius: 3px;
    flex: none;
  }
  .card--brand .brand {
    left: 50%; top: 50%;
    transform: translate(-50%, -62%);
    font-size: 38px;
  }
  .card--brand .brand__square { width: 38px; height: 38px; }
  .card--contact .brand {
    left: 44px; top: 38px;
    font-size: 26px;
  }
  .card--contact .brand__square { width: 26px; height: 26px; }
  .person {
    position: absolute;
    left: 44px; top: 128px;
    font-family: "Alegreya Sans SC", sans-serif;
    color: var(--green);
    font-size: 26px;
  }
  .divider {
    position: absolute;
    left: 44px; right: 44px; top: 172px;
    height: 2px;
    background: var(--blue);
  }
  .contact-list {
    position: absolute;
    right: 44px; top: 196px;
    list-style: none;
    color: var(--green);
    font-size: 19px;
    line-height: 1.55;
  }
  .contact-list li { display: flex; align-items: center; gap: 10px; }
  .contact-list svg { width: 16px; height: 16px; flex: none; }
</style>
</head>
<body>
  <section class="card card--contact">
    <div class="pattern-field pattern-field--edge" role="img" aria-label="Faint triangle lattice pattern along the card edge"></div>
    <div class="pattern-field pattern-field--corner" role="img" aria-label="Faint triangle lattice pattern fading into the corner"></div>
    <div class="brand"><span class="brand__square"></span>Brantley Advisory Group</div>
    <p class="person">Mark Brantley</p>
    <div class="divider"></div>
    <ul class="contact-list">
      <li>
        <svg viewBox="0 0 16 16" aria-hidden="true"><rect x="1" y="1" width="14" height="14" rx="3" fill="#3f5fc6"/><path d="M5 4c-.8.8-.8 2.6 1.4 5s4.2 2.8 5 2l-1.4-1.6-1.2.6c-.8-.4-1.6-1.2-2-2l.6-1.2z" fill="#1f1e20"/></svg>
        425.318.2746
      </li>
      <li>
        <svg viewBox="0 0 16 16" aria-hidden="true"><rect x="1" y="1" width="14" height="14" rx="3" fill="#3f5fc6"/><rect x="3.5" y="5" width="9" height="6.5" fill="none" stroke="#1f1e20" stroke-width="1.2"/><path d="M3.5 5l4.5 3.5L12.5 5" fill="none" stroke="#1f1e20" stroke-width="1.2"/></svg>
        mbrantley@brantleyag-example.com
      </li>
    </ul>
  </section>

  <section class="card card--brand">
    <div class="pattern-field pattern-field--top" role="img" aria-label="Faint triangle lattice pattern in the top corner"></div>
    <div class="pattern-field pattern-field--corner" role="img" aria-label="Faint triangle lattice pattern fading into the corner"></div>
    <div class="brand"><span class="brand__square"></span>Brantley Advisory Group</div>
  </section>
</body>
</html>
```